GUARANTEED 4 sample word cards for inclusive primary education (the swan, the icebear, the cat, sad)

in short: it's about drawing a swan, at icebear, a cat, a sad person (male / female) and arranging them on word cards with some additional information As there which only one design submitted, Which was missing the point I Decided to translate everything myself and upload it again. Requirements Within an open educational ressources (OER) project, materials for the interest-based spelling workout are to be created. In the preparation of this project four example sample word cards are to be developed. Later They Should be compiled dynamically from a database. Since the needs of the teachers are very different, it would be advantageous to integrate the different design elements as layers in Photoshop so did one can show how diverse the cards can look later by hiding / showing the layers. The materials shoulderstand be distributed under cc-0 license. It is about 4 sample cards (the swan, the icebear, the cat, sad), Which shoulderstand demonstrate how search cards can look. German: As part of an OER project are materials to interest-based spelling learning occur. In the preparation of the project (to be created also a permanent position for a / n Designer / -in under which) are four examplarische Sample word cards are developed. Later this should be assembled dynamically from a database. Since the needs of teachers / -Innen are very different, it would be desirable to integrate the various design elements as layers in Photoshop, so you can show how diverse can look the cards later. The materials are to be distributed under cc-0 license. It is about 4 example cards that demonstrate how can such cards look. The most expensive part is undoubtedly the drawings (polar bear, swan, cat and sad child / sad person). Common elements - speech symbol Lindqvist (see http: //media.brenzo-haus. de / media / catalog / product / cache / 4 / image / 3ab41cde77280f19e4c2da6b58190a42 / 0/7 / 07216_1.jpg) - underline articles colored or colored or point mark (male - red, male - blue, neuter - green) - writing of definition and article (once https://typevault.example/en/font/grundschrift and once a school Ausgangsschrift eg https://www.vorlind.example/pulse/Tavrel/de_DE.CMS.displayCMS.209797./die-schulausgangsschrift -sas-free-download-vorlind) - Ruling based on http://www.t-wellbrig.example/wp-content/uploads/2010/01/Heft-006-innen.png (and even without house) - picture on the right side - pictures with people, each as a girl / boy, different skin colors (or all as layers in Photoshop, where I can hide it myself) - syllable sheets (instead of the | http://tryclassmill.example/wp- content / uploads / 2015_2_Silbenboegen_Kombo.png) - colored syllables (blue and red) - stem color (red), ending black - cases if necessary on the back of the card - Format Din A7, rounded corners images should as svg / or levels exist (different skin color / hair color / gender) drawings should stylized and not be too childish and love of detail, so that they are attractive to adults (and as can be used in work with fugitives). You should also black / white and be usable with red / green blindness. The exact requirements are in the description file. For any questions please contact via the platform or paulr.hessling@hs-tarnow.example Ps: If a logo for (spelling) learning, including drops, it is also nich bad;) If you interested in a long-term employment in a project have the university, we appreciate if you mention this.
Target Market(s)
pupils in primary school, so but older students and adults (for example refugees who started to learn the language) students / -Innen primary school (until fourth grade) as well as older adolescents / adults, therefore, not to child pictures
Industry/Entity Type
Education
Font styles to use
Other font styles liked:
- see additional file

Requirements
Must have
- psd files with levels, to show and hide different elements self drawn images, Which Could be released under a CC-0 license. see additional file for more info and sample German: .psd files with labeled layers, in which the individual elements can be hidden. Self-drawn graphics which can then be released under cc-0 Stock

```html
<!DOCTYPE html>
<html lang="de">
<head>
<meta charset="utf-8">
<title>Wortkarte – traurig</title>
<link rel="stylesheet" href="https://fonts.googleapis.com/css2?family=Andika:wght@400;700&display=swap">
<style>
  :root {
    --page-bg: #ffffff;
    --card-frame: #c7dff0;
    --card-face: #ffffff;
    --ink: #0c0c24;
    --ink-soft: #333333;
    --rule: #8a8a8a;
    --house: #a9a9a9;
    --wordclass: #2a6ebb;
    --shadow: rgba(40, 30, 30, 0.55);
  }
  * { margin: 0; padding: 0; box-sizing: border-box; }
  html, body {
    width: 1200px; height: 850px; overflow: hidden;
    background: var(--page-bg);
    font-family: "Andika", sans-serif;
  }
  .word-card {
    position: absolute; left: 98px; top: 71px; width: 1011px; height: 715px;
    background: var(--card-frame);
    box-shadow: 8px 8px 6px var(--shadow);
  }
  .card-face {
    position: absolute; left: 21px; top: 19px; right: 21px; bottom: 22px;
    background: var(--card-face); border-radius: 30px;
  }
  .word-class {
    position: absolute; left: 637px; top: 14px;
    font-size: 37px; line-height: 1.2; color: var(--wordclass); letter-spacing: 0.5px;
  }
  .word-class .marker { font-size: 32px; margin-left: 8px; }
  .illustration {
    position: absolute; left: 571px; top: 96px; width: 376px; height: 314px;
    z-index: 1;
    background: radial-gradient(ellipse at 50% 45%, #e6e6e6 0%, #f5f5f5 60%, rgba(255,255,255,0) 100%);
  }
  .ruling {
    position: absolute; left: 36px; width: 406px; height: 83px; z-index: 2;
  }
  .ruling .line {
    position: absolute; left: 0; right: 0; height: 1px; background: var(--rule);
  }
  .ruling .l1 { top: 0; } .ruling .l2 { top: 26px; }
  .ruling .l3 { top: 57px; } .ruling .l4 { top: 83px; }
  .ruling .house { position: absolute; left: -2px; top: 0; width: 30px; height: 83px; }
  .ruling .word {
    position: absolute; left: 50px; top: 0;
    font-size: 60px; line-height: 1; color: var(--ink); white-space: nowrap;
  }
  .ruling.base { top: 96px; }
  .ruling.comparative { top: 225px; }
  .ruling.superlative { top: 337px; }
  .example-sentence {
    position: absolute; left: 0; right: 0; top: 482px; text-align: center;
    font-size: 60px; color: var(--ink-soft); line-height: 1;
  }
  .tags {
    position: absolute; left: 0; right: 0; top: 591px; text-align: center;
    font-size: 39px; color: var(--ink); line-height: 1;
  }
</style>
</head>
<body>
  <div class="word-card">
    <div class="card-face">
      <div class="word-class">Adjektiv<span class="marker">▲</span></div>

      <div class="illustration" role="img" aria-label="Bleistiftzeichnung: ein trauriger Mann und eine traurige Frau"></div>

      <div class="ruling base">
        <div class="line l1"></div><div class="line l2"></div><div class="line l3"></div><div class="line l4"></div>
        <svg class="house" viewBox="0 0 30 83" aria-hidden="true">
          <path d="M2 82 V24 L15 4 L28 24 V82 Z" fill="none" stroke="var(--house)" stroke-width="2.5"/>
          <rect x="10" y="34" width="8" height="16" fill="none" stroke="var(--house)" stroke-width="1.5"/>
          <path d="M8 60 h4 v5 h4 v5 h4 v5 h4" fill="none" stroke="var(--house)" stroke-width="1.5"/>
        </svg>
        <div class="word">traurig</div>
      </div>

      <div class="ruling comparative">
        <div class="line l1"></div><div class="line l2"></div><div class="line l3"></div><div class="line l4"></div>
        <svg class="house" viewBox="0 0 30 83" aria-hidden="true">
          <path d="M2 82 V24 L15 4 L28 24 V82 Z" fill="none" stroke="var(--house)" stroke-width="2.5"/>
          <rect x="10" y="34" width="8" height="16" fill="none" stroke="var(--house)" stroke-width="1.5"/>
          <path d="M8 60 h4 v5 h4 v5 h4 v5 h4" fill="none" stroke="var(--house)" stroke-width="1.5"/>
        </svg>
        <div class="word">traurig, trauriger,</div>
      </div>

      <div class="ruling superlative">
        <div class="line l1"></div><div class="line l2"></div><div class="line l3"></div><div class="line l4"></div>
        <svg class="house" viewBox="0 0 30 83" aria-hidden="true">
          <path d="M2 82 V24 L15 4 L28 24 V82 Z" fill="none" stroke="var(--house)" stroke-width="2.5"/>
          <rect x="10" y="34" width="8" height="16" fill="none" stroke="var(--house)" stroke-width="1.5"/>
          <path d="M8 60 h4 v5 h4 v5 h4 v5 h4" fill="none" stroke="var(--house)" stroke-width="1.5"/>
        </svg>
        <div class="word">am traurigsten</div>
      </div>

      <p class="example-sentence">Das Kind ist traurig.</p>
      <p class="tags">Stimmung | Mensch | Gefühl</p>
    </div>
  </div>
</body>
</html>
```